Brazilian publishing house needs a JAZZY poster

We're launching an international guerrilla marketing campaign for a biography about the greatest saxophonist ever, Dorian Mabry (also known as "Tusk"), so we need a poster that will be printed and pasted on walls and posts, on a regular sheet, size A4.

It must say "Tusk vive!" (which means "Tusk lives!" in Portuguese) and have the website, www.qvzt.example/tuskvive. All the rest is free. Jazzy, MINIMALIST, cool images with birds and saxophones (or birds becoming saxophones) are welcome. Also, please insert our logo (attached) somewhere, even if not big.

I like this campaign very much and you like something like that: https://pomeraltisca.strovelpress.example/

Hope to hear from you!

Marketing

• Easy to see and understand, like most guerrilla actions, without many colors

```html
<!DOCTYPE html>
<html lang="pt">
<head>
<meta charset="utf-8">
<title>Tusk vive! — poster</title>
<link rel="stylesheet" href="https://fonts.googleapis.com/css2?family=Righteous&family=Questrial&display=swap">
<style>
  :root {
    --paper: #ffffff;
    --wine: #7b0008;
    --amber: #d8820f;
    --ink: #151515;
    --bar: #4a4a4a;
    --bar-text: #ffffff;
    --peach: #f3c9a0;
    --suit: #8f9a8c;
    --shadow: #2a1f1a;
  }
  * { margin: 0; padding: 0; box-sizing: border-box; }
  html, body {
    width: 800px;
    height: 1200px;
    overflow: hidden;
    background: var(--paper);
  }
  .poster {
    position: relative;
    width: 800px;
    height: 1200px;
    background: var(--paper);
    overflow: hidden;
  }
  .confetti-field {
    position: absolute;
    left: 0;
    top: 20px;
    width: 520px;
    height: 800px;
    background: radial-gradient(ellipse at 55% 50%, rgba(243, 201, 160, 0.55) 0%, rgba(243, 201, 160, 0.25) 45%, rgba(255, 255, 255, 0) 72%);
  }
  .portrait {
    position: absolute;
    left: 170px;
    top: 85px;
    width: 490px;
    height: 610px;
    border-radius: 120px 120px 0 0;
    background:
      linear-gradient(to bottom, rgba(255,255,255,0) 0%, rgba(255,255,255,0) 78%, var(--paper) 100%),
      linear-gradient(100deg, #b98a3e 0%, var(--shadow) 30%, var(--suit) 55%, #b7bfb0 80%, var(--suit) 100%);
  }
  .headline {
    position: absolute;
    left: 0;
    top: 640px;
    width: 800px;
    height: 470px;
  }
  .headline text {
    font-family: "Righteous", sans-serif;
  }
  .headline .name { fill: var(--wine); }
  .headline .verb { fill: var(--amber); }
  .publisher {
    position: absolute;
    left: 0;
    top: 1106px;
    width: 800px;
    text-align: center;
    font-family: "Questrial", sans-serif;
    font-size: 38px;
    letter-spacing: 3px;
    color: var(--ink);
    line-height: 1;
  }
  .site-bar {
    position: absolute;
    left: 265px;
    top: 1152px;
    width: 270px;
    height: 30px;
    background: var(--bar);
    color: var(--bar-text);
    font-family: "Questrial", sans-serif;
    font-size: 17px;
    line-height: 30px;
    text-align: center;
    white-space: nowrap;
  }
</style>
</head>
<body>
  <main class="poster">
    <div class="confetti-field" role="img" aria-label="Scattered soft peach squares drifting behind the musician"></div>
    <div class="portrait" role="img" aria-label="Photograph of Dorian Mabry in a grey suit playing a brass alto saxophone, orange musical flames rising from the bell"></div>

    <svg class="headline" viewBox="0 0 800 470" width="800" height="470" aria-label="Tusk vive!">
      <text class="name" x="105" y="218" font-size="280" textLength="655" lengthAdjust="spacingAndGlyphs">TUSK</text>
      <text class="verb" x="55" y="455" font-size="290" textLength="705" lengthAdjust="spacingAndGlyphs">VIVE!</text>
    </svg>

    <div class="publisher">VELDMARK</div>
    <div class="site-bar">www.qvzt.example/tuskvive</div>
  </main>
</body>
</html>
```